Redo of existing website www.brontivel.com

I would like it to look like the newer style website, with large images, less text. clean and modern looking. The new design should focus on call to action. ultimately that's what were looking for.Some features I would like to see we try to do good job of keeping up with our blog, and it is a good source of recent pictures of our work. I like four visitors to get the few pieces they're doing with a national brand or franchise pray. I like to stay far from the idea of a local one-man band with magnetic signs on his truck.
I think that clean beautiful images have the biggest impact. In my opinion most people don't read more than a couple lines of text. The text is more for search engines.
we are currently in the process of revising our logo as well, I will upload those files when I get them.
Please feel free to use content and images from our current website www.brontivel.com. we can purchase professional stock images if needed.
1. large call to action with easy contact form.
2. Blog roll on front page to showcase our recent work.
2. All social connect buttons.
Check out our reviews on zindexa!
My current websites
Www.brontivel.com
https://plus.vorplink.com/593028416627304918735/about
www.chatterbook.com/brontivel
http://www.skimblr.com/blog/curbmarauder
https://chirpfeed.com/Brontivel
websites I like the way they look.
http://postwren.com/
http://www.vendlio.com/
http://www.corvanblacktop.com/
http://www.tarwayguild.org/
http://groundsurfacecrafts.com/
Updates
Hello all,
I have just uploaded some images of our company mascot "Curb Marauder" and our new logo.
Project Deadline Extended
Reason: Death in family. Finally back to work.
Target Market(s)
We have 2 main groups of customers commercial and residential.
Commercial customers are Property owners and managers, operators of multi location business, restaurant, supermarket, banks, and are best source for repeat business
for Residential customers we provide driveway repair and driveway paving services.
for residential customers I would like to encourge the submission or pictures with the inquiry for a quick quote. Residential customers are typically a one time job but are a good source of referrals
I like how this website separates residential and commercial
http://www.glintcoatdirect.com
Industry/Entity Type
Call
Look and feel
Each slider illustrates characteristics of the customer's brand and the style your logo design should communicate.

```html
<!DOCTYPE html>
<html lang="en">
<head>
<meta charset="utf-8">
<title>Brontivel — Services</title>
<link rel="stylesheet" href="https://fonts.googleapis.com/css2?family=Prata&family=Ubuntu:wght@400;500&family=Lato:ital@1&display=swap">
<style>
:root{
  --green:#00dd00;
  --bg-dark:#222222;
  --bg-form:#262626;
  --card:#252525;
  --field:#3a3a3a;
  --button:#4a4a4a;
  --text:#8a8a8a;
  --muted:#555555;
  --white:#ffffff;
}
*{box-sizing:border-box;margin:0;padding:0}
html,body{width:1108px;height:1200px;overflow:hidden;background:var(--bg-dark)}
body{position:relative;font-family:"Ubuntu",sans-serif;color:var(--text)}
.section{position:absolute;left:0;width:1108px}
.commercial{top:0;height:511px}
.commercial-photo{position:absolute;inset:0;background:linear-gradient(100deg,#5a5a58 0%,#3e3f3c 30%,#2d2e2a 55%,#4a4840 75%,#57544c 100%)}
.commercial-photo::after{content:"";position:absolute;inset:0;background:rgba(20,20,20,.35)}
.residential{top:511px;height:318px;background:var(--bg-dark)}
.estimate{top:829px;height:371px;background:var(--bg-form)}
.section-head{position:absolute;left:0;width:100%;text-align:center}
.section-head .rule{display:block;width:18px;height:1px;background:var(--green);margin:0 auto 10px}
.section-title{font-family:"Prata",serif;font-weight:400;font-size:27px;letter-spacing:.5px;color:var(--green);line-height:1}
.commercial .section-title{color:var(--white)}
.commercial .rule{background:var(--white)}
.section-sub{font-family:"Lato",sans-serif;font-style:italic;font-size:9.5px;color:var(--muted);margin-top:8px}
.commercial .section-sub{color:#9a9a9a}
.card{position:absolute;width:248px;background:var(--card)}
.card.active{background:var(--green)}
.card .thumb{position:absolute;left:-30px;width:62px;height:62px;transform:rotate(45deg);border:2px solid var(--white);border-radius:8px;background:radial-gradient(circle at 40% 40%,#8a7d55,#5d5536 60%,#3e3a26);overflow:hidden}
.card .body{position:absolute;left:70px;right:40px}
.card .rule{display:block;width:18px;height:1px;background:var(--green);margin-bottom:6px}
.card.active .rule{background:var(--white)}
.card h3{font-family:"Prata",serif;font-weight:400;font-size:12.5px;line-height:13px;color:var(--green);text-transform:uppercase}
.card.active h3{color:var(--white)}
.card p{font-size:9.5px;line-height:13.5px;margin-top:6px}
.card.active p{color:var(--white);font-weight:500}
.card .more{position:absolute;left:70px;right:40px;border-top:1px solid #333;padding-top:11px;font-family:"Prata",serif;font-size:8.5px;color:#6d6d6d;display:flex;align-items:center;gap:6px}
.card.active .more{border-top-color:rgba(255,255,255,.5);color:var(--white);font-family:"Ubuntu",sans-serif;font-weight:500}
.intro{position:absolute;top:133px;width:466px;font-size:9.6px;line-height:13.4px;color:#8a8a8a}
.btn{position:absolute;background:var(--button);color:var(--white);font-family:"Prata",serif;font-size:9px;display:flex;align-items:center;justify-content:center;gap:8px;letter-spacing:.2px}
.form-title{position:absolute;left:75px;top:132px;font-family:"Prata",serif;font-size:12.5px;color:var(--green)}
.form-note{position:absolute;left:75px;top:147px;font-size:9.5px;color:#8a8a8a}
.field{position:absolute;width:303px;height:31px;background:var(--field);font-size:8.5px;color:#777;padding:11px 0 0 17px}
.field.tall{height:122px}
.call-note{position:absolute;left:91px;top:325px;font-size:9.5px;color:#8a8a8a}
</style>
</head>
<body>

<section class="section commercial">
  <div class="commercial-photo" role="img" aria-label="Photo of a paving crew at work beside a skid-steer loader and a metal building"></div>
  <div class="section-head" style="top:53px">
    <span class="rule"></span>
    <h2 class="section-title">COMMERCIAL</h2>
    <p class="section-sub">Curabitur quis lorem augue. Phasellus sit amet sagittis nisl.</p>
  </div>

  <article class="card" style="left:130px;top:137px;height:141px">
    <div class="thumb" role="img" aria-label="Service photo" style="top:40px"></div>
    <div class="body" style="top:20px"><span class="rule"></span><h3>Coating</h3><p>Nullam vulputate a lacus at pretium. Sed porta nunc sit amet eros sollicitudin</p></div>
    <div class="more" style="top:98px">LEARN MORE <svg width="11" height="7" viewBox="0 0 11 7"><ellipse cx="5.5" cy="3.5" rx="5" ry="3" fill="none" stroke="currentColor"/><circle cx="5.5" cy="3.5" r="1.4" fill="currentColor"/></svg></div>
  </article>
  <article class="card active" style="left:459px;top:137px;height:141px">
    <div class="thumb" role="img" aria-label="Service photo" style="top:40px"></div>
    <div class="body" style="top:20px"><span class="rule"></span><h3>Striping</h3><p>Nullam vulputate a lacus at pretium. Sed porta nunc sit amet eros sollicitudin</p></div>
    <div class="more" style="top:98px">LEARN MORE <svg width="11" height="7" viewBox="0 0 11 7"><ellipse cx="5.5" cy="3.5" rx="5" ry="3" fill="none" stroke="currentColor"/><circle cx="5.5" cy="3.5" r="1.4" fill="currentColor"/></svg></div>
  </article>
  <article class="card" style="left:788px;top:137px;height:141px">
    <div class="thumb" role="img" aria-label="Service photo" style="top:40px"></div>
    <div class="body" style="top:20px"><span class="rule"></span><h3>Crack Filling</h3><p>Nullam vulputate a lacus at pretium. Sed porta nunc sit amet eros sollicitudin</p></div>
    <div class="more" style="top:98px">LEARN MORE <svg width="11" height="7" viewBox="0 0 11 7"><ellipse cx="5.5" cy="3.5" rx="5" ry="3" fill="none" stroke="currentColor"/><circle cx="5.5" cy="3.5" r="1.4" fill="currentColor"/></svg></div>
  </article>

  <article class="card" style="left:130px;top:307px;height:155px">
    <div class="thumb" role="img" aria-label="Service photo" style="top:47px"></div>
    <div class="body" style="top:20px"><span class="rule"></span><h3>Parking Lot<br>Paving</h3><p>Nullam vulputate a lacus at pretium. Sed porta nunc sit amet eros sollicitudin</p></div>
    <div class="more" style="top:112px">LEARN MORE <svg width="11" height="7" viewBox="0 0 11 7"><ellipse cx="5.5" cy="3.5" rx="5" ry="3" fill="none" stroke="currentColor"/><circle cx="5.5" cy="3.5" r="1.4" fill="currentColor"/></svg></div>
  </article>
  <article class="card" style="left:459px;top:307px;height:155px">
    <div class="thumb" role="img" aria-label="Service photo" style="top:47px"></div>
    <div class="body" style="top:20px"><span class="rule"></span><h3>Parking Lot<br>Repairs</h3><p>Nullam vulputate a lacus at pretium. Sed porta nunc sit amet eros sollicitudin</p></div>
    <div class="more" style="top:112px">LEARN MORE <svg width="11" height="7" viewBox="0 0 11 7"><ellipse cx="5.5" cy="3.5" rx="5" ry="3" fill="none" stroke="currentColor"/><circle cx="5.5" cy="3.5" r="1.4" fill="currentColor"/></svg></div>
  </article>
  <article class="card" style="left:788px;top:307px;height:155px">
    <div class="thumb" role="img" aria-label="Service photo" style="top:47px"></div>
    <div class="body" style="top:20px"><span class="rule"></span><h3>Asphalt<br>Maintenance</h3><p>Nullam vulputate a lacus at pretium. Sed porta nunc sit amet eros sollicitudin</p></div>
    <div class="more" style="top:112px">LEARN MORE <svg width="11" height="7" viewBox="0 0 11 7"><ellipse cx="5.5" cy="3.5" rx="5" ry="3" fill="none" stroke="currentColor"/><circle cx="5.5" cy="3.5" r="1.4" fill="currentColor"/></svg></div>
  </article>
</section>

<section class="section residential">
  <div class="section-head" style="top:48px">
    <span class="rule"></span>
    <h2 class="section-title">RESIDENTIAL</h2>
    <p class="section-sub">Curabitur quis lorem augue. Phasellus sit amet sagittis nisl.</p>
  </div>
  <p class="intro" style="left:75px">Lorem ipsum dolor sit amet, consectetur adipiscing elit. Ut et nibh luctus, tincidunt ante non, ultricies ante. Donec tincidunt dolor a pharetra congue. Sed ultrices libero ac ante blandit, et porttitor massa feugiat.<br>Vestibulum ante ipsum primis in faucibus orci luctus et ultrices posuere cubilia Curae; Nulla bibendum massa eget pellentesque placerat. Mauris aliquam posuere enim vitae rutrum. Cum sociis natoque penatibus et magnis dis parturient montes, nascetur ridiculus mus.</p>
  <p class="intro" style="left:567px">Lorem ipsum dolor sit amet, consectetur adipiscing elit. Ut et nibh luctus, tincidunt ante non, ultricies ante. Donec tincidunt dolor a pharetra congue. Sed ultrices libero ac ante blandit, et porttitor massa feugiat.<br>Vestibulum ante ipsum primis in faucibus orci luctus et ultrices posuere cubilia Curae; Nulla bibendum massa eget pellentesque placerat. Mauris aliquam posuere enim vitae rutrum. Cum sociis natoque penatibus et magnis dis parturient montes, nascetur ridiculus mus.</p>
  <div class="btn" style="left:496px;top:245px;width:118px;height:24px">VIEW MORE <svg width="12" height="7" viewBox="0 0 12 7"><path d="M1 1l5 5 5-5" fill="none" stroke="#fff" stroke-width="1.3"/></svg></div>
</section>

<section class="section estimate">
  <div class="section-head" style="top:50px">
    <span class="rule"></span>
    <h2 class="section-title">FREE ESTIMATE</h2>
    <p class="section-sub">Curabitur quis lorem augue. Phasellus sit amet sagittis nisl.</p>
  </div>
  <h3 class="form-title">CONTACT FORM</h3>
  <p class="form-note">Please provide us information about your specific asphalt repair, paving, resurfacing, or seal coating needs and we will provide you a quote via email within 3 business days.</p>
  <div class="field" style="left:75px;top:174px">Name</div>
  <div class="field" style="left:75px;top:220px">Email</div>
  <div class="field" style="left:75px;top:265px">Phone Number</div>
  <div class="field" style="left:402px;top:174px">Address</div>
  <div class="field" style="left:402px;top:220px">City</div>
  <div class="field" style="left:402px;top:265px">Zip Code</div>
  <div class="field tall" style="left:731px;top:174px">Description</div>
  <p class="call-note">If you have any questions about your asphalt repair, paving, resurfacing, or sealing needs please call us at 555-014-2267</p>
  <div class="btn" style="left:869px;top:311px;width:166px;height:24px">GET YOUR FREE ESTIMATE</div>
</section>

</body>
</html>
```